Home Page Website Design

The Site width is 1000 px. I've attached a Balsamiq mockup as a design layout guide. The design needs to be flat and clean. Please stick to the pixel dimensions of the mock up as the site will be responsive. I've also attached the logos used on the mockup for positional purposes.

Colours to use: Black, Grey, Green (Logo tie in) & green complementary colours.

Green (Logo tie in)
White Background
Titles: Black (Roboto Bold 700)
Text: Dark Grey (Roboto Normal 400)

Look & Style Example
http://www.brindlevox.org.uk/

Type Face
Google Fonts - Roboto

These are just guidelines, please feel free to use you own creative judgment.

Thanks

```html
<!DOCTYPE html>
<html lang="en">
<head>
<meta charset="utf-8">
<title>Brindlevox Teaching School Alliance – Home</title>
<link href="https://fonts.googleapis.com/css2?family=Roboto:wght@400;500;700&display=swap" rel="stylesheet">
<style>
:root{
  --green:#0a9a3c;
  --green-dark:#087a2f;
  --green-light:#17ad4a;
  --ink:#1c1c1c;
  --text:#444;
  --grey-bg:#efefef;
  --grey-line:#d9d9d9;
  --nav:#2b2b2b;
  --btn-dark:#3a3a3a;
}
*{box-sizing:border-box;margin:0;padding:0}
html,body{width:1000px;height:1200px;overflow:hidden}
body{font-family:'Roboto',Arial,sans-serif;color:var(--text);background:#f6f6f6;position:relative;font-size:10px}
.abs{position:absolute}
a{color:inherit;text-decoration:none}

/* header */
.brand{left:108px;top:34px;display:flex;align-items:center;gap:8px}
.brand-mark{width:26px;height:26px;background:var(--green)}
.brand-name{font-size:17px;font-weight:500;color:var(--green);line-height:1.1;width:180px}
.login{left:843px;top:11px;width:49px;height:26px;border:1px solid #cfcfcf;border-radius:3px;background:#f4f4f4;font-size:10px;font-weight:500;color:#333;display:flex;align-items:center;justify-content:center}
.chat{left:508px;top:70px;display:flex;align-items:center;gap:8px;color:var(--green);font-weight:700;font-size:12px}
.chat-dot{width:30px;height:22px;border-radius:50%;background:#f07a1e}
.divider{left:626px;top:48px;width:1px;height:50px;background:#ddd}
.register-title{left:642px;top:49px;font-size:12px;color:#333;font-weight:500}
.email{left:642px;top:70px;width:183px;height:26px;border:1px solid #ccc;border-radius:3px;background:#f0f0f0;font-style:italic;font-size:9.5px;color:#999;padding:8px 11px}
.submit{left:833px;top:70px;width:58px;height:26px;border-radius:3px;background:var(--green);color:#fff;font-weight:700;font-size:10px;display:flex;align-items:center;justify-content:center}

/* nav */
.nav{left:108px;top:116px;width:784px;height:40px;background:var(--nav);border-radius:3px;border:1px solid #111}
.nav a{position:absolute;top:13px;color:#fff;font-size:9.5px;font-weight:400;white-space:nowrap;line-height:12px}
.search{position:absolute;right:9px;top:9px;width:125px;height:20px;background:#fff;border-radius:3px;font-size:9px;color:#999;padding:5px 10px}
.search svg{position:absolute;right:6px;top:4px}

/* hero */
.hero{left:108px;top:160px;width:784px;height:305px;border-radius:3px;overflow:hidden;background:linear-gradient(120deg,#c9b08e 0%,#8e7a62 30%,#d9cbb8 55%,#6f5d4c 80%,#b79b86 100%)}
.hero-panel{position:absolute;left:17px;top:17px;width:233px;height:272px;background:rgba(255,255,255,.88);border-radius:4px;padding:14px 16px}
.hero-panel h1{font-size:23px;line-height:23px;font-weight:500;color:var(--green);margin-bottom:12px}
.hero-panel p{font-size:10.5px;line-height:16.7px;color:#333}
.hero-btn{position:absolute;left:16px;top:218px;width:116px;height:32px;background:var(--btn-dark);border-radius:3px;color:#fff;font-size:11.5px;display:flex;align-items:center;justify-content:center}
.hero-arrows{position:absolute;right:10px;bottom:16px;display:flex;gap:6px}
.round{width:26px;height:26px;border-radius:50%;background:#fff;display:flex;align-items:center;justify-content:center;box-shadow:0 1px 2px rgba(0,0,0,.3)}

/* band */
.band{left:0;top:480px;width:1000px;height:389px;background:linear-gradient(#efefef,#fafafa)}
.card{background:#fff;border:1px solid var(--grey-line);border-radius:3px}
.card h2{font-size:17px;font-weight:500;color:var(--ink)}
.welcome{left:108px;top:493px;width:251px;height:355px;padding:10px 14px}
.video{margin-top:10px;width:222px;height:141px;border:2px solid #ddd;background:linear-gradient(135deg,#a79a88,#5d5247 50%,#8a7c6e);position:relative}
.video .play{position:absolute;left:88px;top:38px}
.welcome p{margin-top:12px;font-size:9.5px;line-height:16.6px;color:#444}
.read-more{display:block;margin-top:14px;color:var(--green);font-weight:500;font-size:9.5px}

.training{left:375px;top:493px;width:251px;height:223px;padding:10px 15px}
.training ul{list-style:none;margin-top:10px}
.training li{height:32px;margin-bottom:3px;background:linear-gradient(var(--green-light),var(--green-dark));border-radius:2px;color:#fff;font-size:12px;font-weight:500;display:flex;align-items:center;justify-content:space-between;padding:0 10px 0 13px}
.chev{width:16px;height:16px;border-radius:50%;background:rgba(255,255,255,.85);display:flex;align-items:center;justify-content:center}

.news{left:375px;top:727px;width:251px;height:121px;padding:10px 15px}
.news .ctrl{position:absolute;right:13px;top:16px;display:flex;gap:8px}
.news h3{margin-top:8px;font-size:12px;line-height:16.5px;font-weight:500;color:var(--green)}
.news p{font-size:9.5px;line-height:16.5px;color:#333;margin-top:2px}

.courses{left:642px;top:493px;width:251px;height:355px;padding:10px 14px}
.course-list{position:absolute;left:12px;top:39px;width:214px;height:302px;overflow:hidden}
.course{border:1px solid #ccc;border-radius:2px;background:#f7f7f7;padding:9px 11px;margin-bottom:8px;height:114px;position:relative}
.course h3{font-size:12px;line-height:16.5px;font-weight:500;color:var(--green)}
.course p{font-size:9.5px;line-height:16.5px;color:#444;margin-top:1px}
.places{position:absolute;left:11px;bottom:14px;color:var(--green);font-weight:700;font-size:9.5px}
.book{position:absolute;right:17px;bottom:10px;width:54px;height:22px;background:var(--btn-dark);border-radius:2px;color:#fff;font-size:9.5px;display:flex;align-items:center;justify-content:center}
.scrollbar{position:absolute;left:234px;top:39px;width:10px;height:302px;background:#e4e4e4}
.scrollbar span{display:block;height:18px;background:var(--green)}

/* footer */
.footer{left:0;top:869px;width:1000px;height:206px;background:#e9e9e9}
.f-col{font-size:10px;line-height:17.5px;color:#333}
.f-title{color:var(--green);font-weight:500;margin-bottom:4px}
.green{color:var(--green)}
.f-address{left:108px;top:884px}
.f-nav{left:367px;top:884px}
.f-nav .cols{display:flex;gap:32px;line-height:21px}
.f-social{left:642px;top:884px}
.social{display:flex;gap:18px;align-items:center;margin-top:4px}
.social span{display:flex;align-items:center;gap:7px}
.sq{width:18px;height:18px;background:#3b6bb0;border-radius:2px}
.sq.light{background:#59a9d9}
.hub{margin-top:14px;display:flex;align-items:center;gap:8px;font-size:14px;line-height:16.5px;color:#222;width:130px}
.hub-dot{width:30px;height:30px;border-radius:50%;background:#8fc23f;flex:none}

.partners{left:108px;top:1044px;width:784px;height:108px;background:linear-gradient(#fff,#e6e6e6);border:1px solid #ddd;border-radius:3px;display:flex;align-items:center;justify-content:space-around;padding:0 12px}
.badge{background:#ccc}
.copyright{left:0;top:1170px;width:1000px;text-align:center;font-size:10px;color:#333}
</style>
</head>
<body>

<header>
  <div class="abs brand"><div class="brand-mark"></div><div class="brand-name">Brindlevox Teaching School Alliance</div></div>
  <a class="abs login" href="#">LOG IN</a>
  <div class="abs chat"><span class="chat-dot"></span>LIVE CHAT</div>
  <div class="abs divider"></div>
  <div class="abs register-title">REGISTER NOW</div>
  <div class="abs email">enter email address</div>
  <a class="abs submit" href="#">SUBMIT</a>
</header>

<nav class="abs nav">
  <a href="#" style="left:11px">HOME</a>
  <a href="#" style="left:57px">ABOUT US</a>
  <a href="#" style="left:124px">TRAINING &amp; DEVELOPMENT</a>
  <a href="#" style="left:266px">BENEFITS</a>
  <a href="#" style="left:332px">MEMBERS</a>
  <a href="#" style="left:400px">WHATS ON</a>
  <a href="#" style="left:474px">NEWS</a>
  <a href="#" style="left:524px">FORUM</a>
  <a href="#" style="left:581px">CONTACT US</a>
  <div class="search">Search...
    <svg width="14" height="14" viewBox="0 0 14 14"><circle cx="5.5" cy="5.5" r="4" fill="none" stroke="#0a9a3c" stroke-width="2"/><line x1="8.5" y1="8.5" x2="13" y2="13" stroke="#0a9a3c" stroke-width="2.4"/></svg>
  </div>
</nav>

<section class="abs hero" role="img" aria-label="Teachers working together around classroom tables in a workshop">
  <div class="hero-panel">
    <h1>New Teachers in Workshops</h1>
    <p>Vestibulum vel metus sit amet turpis bibendum tincidunt vel sit amet quam. Pellentesque habitant morbi tristique senectus et netus et malesuada fames ac turpis egestas. Nunc consequat congue nulla eu imperdiet. Donec in est erat, id malesuada turpis. Nunc a dui id turpis convallis semper.</p>
    <a class="hero-btn" href="#">FIND OUT MORE</a>
  </div>
  <div class="hero-arrows">
    <span class="round"><svg width="10" height="12" viewBox="0 0 10 12"><path d="M7 1 2 6l5 5" fill="none" stroke="#333" stroke-width="2.2"/></svg></span>
    <span class="round"><svg width="10" height="12" viewBox="0 0 10 12"><path d="M3 1l5 5-5 5" fill="none" stroke="#333" stroke-width="2.2"/></svg></span>
  </div>
</section>

<div class="abs band"></div>

<section class="abs card welcome">
  <h2>Welcome</h2>
  <div class="video" role="img" aria-label="Video still of a large group of teachers seated in a training hall">
    <svg class="play" width="46" height="46" viewBox="0 0 46 46"><circle cx="23" cy="23" r="22" fill="rgba(255,255,255,.55)"/><path d="M18 13l14 10-14 10z" fill="#fff"/></svg>
  </div>
  <p>Vestibulum vel metus sit amet turpis bibendum tincidunt vel sit amet quam. Pellentesque habitant morbi tristique senectus et netus et malesuada fames ac turpis egestas. Nunc consequat congue nulla eu imperdiet. Donec in est erat, id malesuada turpis. Nunc a dui id turpis convallis semper.</p>
  <a class="read-more" href="#">READ MORE</a>
</section>

<section class="abs card training">
  <h2>Training &amp; Development</h2>
  <ul>
    <li>Leadership Training<span class="chev"><svg width="6" height="8" viewBox="0 0 6 8"><path d="M1 1l3 3-3 3" fill="none" stroke="#555" stroke-width="1.6"/></svg></span></li>
    <li>CPD<span class="chev"><svg width="6" height="8" viewBox="0 0 6 8"><path d="M1 1l3 3-3 3" fill="none" stroke="#555" stroke-width="1.6"/></svg></span></li>
    <li>School to School Support<span class="chev"><svg width="6" height="8" viewBox="0 0 6 8"><path d="M1 1l3 3-3 3" fill="none" stroke="#555" stroke-width="1.6"/></svg></span></li>
    <li>Research &amp; Development<span class="chev"><svg width="6" height="8" viewBox="0 0 6 8"><path d="M1 1l3 3-3 3" fill="none" stroke="#555" stroke-width="1.6"/></svg></span></li>
    <li>ITT &nbsp;( School Direct )<span class="chev"><svg width="6" height="8" viewBox="0 0 6 8"><path d="M1 1l3 3-3 3" fill="none" stroke="#555" stroke-width="1.6"/></svg></span></li>
  </ul>
</section>

<section class="abs card news">
  <h2>News</h2>
  <div class="ctrl">
    <svg width="7" height="10" viewBox="0 0 7 10"><path d="M5.5 1 1.5 5l4 4" fill="none" stroke="#444" stroke-width="1.6"/></svg>
    <svg width="7" height="10" viewBox="0 0 7 10"><path d="M1.5 1l4 4-4 4" fill="none" stroke="#444" stroke-width="1.6"/></svg>
  </div>
  <h3>Lorem ipsum dolor sit amet, consectetur adipiscing elit.</h3>
  <p>Aliquam molestie, mi et imperdiet euismod, dui purus auctor tellus..</p>
</section>

<section class="abs card courses">
  <h2>Latest Courses</h2>
  <div class="course-list">
    <article class="course">
      <h3>Want to deliver consistently ‘Outstanding’ Lessons?</h3>
      <p>Aliquam molestie, mi et imperdiet euismod, dui purus auctor tellus..</p>
      <span class="places">6 Places Left</span><a class="book" href="#">BOOK</a>
    </article>
    <article class="course">
      <h3>School direct intial Teacher Training Places still available.</h3>
      <p>Aliquam molestie, mi et imperdiet euismod, dui purus auctor tellus..</p>
      <span class="places">2 Places Left</span><a class="book" href="#">BOOK</a>
    </article>
    <article class="course">
      <h3>Take a look our Newly Qualified Teacher Learning Pacakges.</h3>
      <p>Aliquam molestie, mi et imperdiet euismod, dui purus auctor tellus..</p>
    </article>
  </div>
  <div class="scrollbar"><span></span></div>
</section>

<footer>
  <div class="abs footer"></div>
  <div class="abs f-col f-address">
    <div class="f-title">Brindlevox Teaching School Alliance</div>
    Harrow Lane<br>Brindleford<br>BX4 7QT<br>
    <span class="green">Tel:</span> 01632 960418<br>
    <span class="green">Email:</span> brindlevox.org.uk
  </div>
  <div class="abs f-col f-nav">
    <div class="f-title">Navigation</div>
    <div class="cols">
      <div>About Us<br>Training &amp; Development<br>Benefits<br>Members</div>
      <div>Calender of Events<br>Contact Us<br>News<br>Forum<br>Site Map</div>
    </div>
  </div>
  <div class="abs f-col f-social">
    <div class="f-title">Navigation</div>
    <div class="social">
      <span><i class="sq"></i>Townsquare</span>
      <span><i class="sq light"></i>Chirpline</span>
    </div>
    <div class="hub"><span class="hub-dot"></span>Regional Teaching Hub</div>
  </div>

  <div class="abs partners" aria-label="Partner schools and organisations">
    <span class="badge" style="width:53px;height:53px;background:#2a3a9c"></span>
    <span class="badge" style="width:104px;height:53px;background:#8b6a4f"></span>
    <span class="badge" style="width:112px;height:44px;background:#c9c9c9;border-radius:22px"></span>
    <span class="badge" style="width:42px;height:52px;background:#7d8bb0"></span>
    <span class="badge" style="width:48px;height:52px;background:#ef6a3a;border-radius:50%"></span>
    <span class="badge" style="width:115px;height:52px;background:#b8c2d6"></span>
    <span class="badge" style="width:42px;height:48px;background:#23407a"></span>
    <span class="badge" style="width:38px;height:52px;background:#a9a9a9"></span>
    <span class="badge" style="width:50px;height:56px;background:#2d5d9a;border-radius:50%"></span>
  </div>

  <div class="abs copyright">Copyright © 2013. <span class="green">Brindlevox Teaching School</span>. All Right Reserved</div>
</footer>

</body>
</html>
```